Brightfern Supports

We need an updated website that captures the comprehensive services and supports we provide to persons with developmental disabilities. We need a website design that educates families about the services we provide. We would also need a website that is user-friendly so that we could periodically update training schedules and ongoing programming.

• Thank you for submitting designs.  A few things I am hoping to see offered in the website:
• Front page highlights the services we offer (host homes, family caregiver, day program, employment program, SLS program, supported apartment program, behavior/clinical program)
• Front page also highlights any new programs we want to make prominent:  family caregiver, future restaurant employment openings, etc...
• Interactive Training Calendar
• Employee Resources page (link to carelyn, email login, etc.)
• Uniform provider application for host home providers
• Information on agency - history, goals, etc.
• Contact Information/Location

 

Fun things to include:

• Client Highlights (featuring a client story each month, etc...)
• Employee highlights (featuring a staff member...)
• link to other Brightfern business pages (Brightfern Therapy and Brightfern Restaurant)

```html
<!DOCTYPE html>
<html lang="en">
<head>
<meta charset="utf-8">
<title>Brightfern Supports</title>
<link rel="stylesheet" href="https://fonts.googleapis.com/css2?family=Open+Sans:wght@400;600;700&display=swap">
<style>
:root{
  --brand:#7d1c1f;
  --brand-dark:#5e1214;
  --nav-top:#b23a3a;
  --nav-bottom:#8a2123;
  --text:#555;
  --light:#ebebeb;
  --footer:#1c1c1c;
  --field-border:#d6d6d6;
  --btn-top:#5a5a5a;
  --btn-bottom:#2e2e2e;
}
*{box-sizing:border-box;margin:0;padding:0}
html,body{width:982px;height:1200px;overflow:hidden}
body{font-family:"Open Sans",Arial,sans-serif;background:#fff;color:var(--text);position:relative}
.site-header{position:absolute;left:0;top:0;width:982px;height:116px;background:#fff}
.brand{position:absolute;left:83px;top:34px;display:flex;align-items:center;gap:10px}
.brand-mark{width:22px;height:22px;background:var(--brand);border-radius:50%}
.brand-name{font-size:26px;font-weight:700;color:var(--brand);letter-spacing:.2px}
.call{position:absolute;right:83px;top:20px;text-align:right;padding-right:34px}
.call-label{font-size:13px;color:#555;line-height:16px}
.call-number{font-size:17px;font-weight:600;color:var(--brand);line-height:20px}
.call svg{position:absolute;right:0;top:8px}
.search{position:absolute;left:757px;top:68px;width:141px;height:26px;border:1px solid #d8d8d8;border-radius:3px;background:#fff}
.search span{position:absolute;left:12px;top:5px;font-size:11px;color:#888}
.search svg{position:absolute;right:5px;top:4px}
.search i{position:absolute;right:25px;top:4px;width:1px;height:17px;background:#ddd}
.main-nav{position:absolute;left:0;top:116px;width:982px;height:38px;background:linear-gradient(var(--nav-top),var(--nav-bottom))}
.main-nav ul{list-style:none;position:absolute;left:82px;top:0;display:flex;height:38px}
.main-nav li{height:38px;display:flex;align-items:center;justify-content:center;color:#fff;font-size:13.5px;font-weight:600;text-transform:uppercase;border-right:1px solid var(--brand-dark)}
.main-nav li.active{background:var(--brand-dark)}
.hero{position:absolute;left:0;top:154px;width:982px;height:423px;background:linear-gradient(170deg,#4f86d6 0%,#8ab3e6 35%,#c9d3dc 55%,#7a7770 75%,#4e4a45 100%)}
.hero-caption{position:absolute;left:82px;top:158px;width:315px;height:107px;background:rgba(40,40,40,.8);border-radius:3px;padding:7px 11px}
.hero-caption p{color:#fff;font-size:19.5px;line-height:32.5px;text-transform:uppercase}
.hero-next{position:absolute;left:872px;top:198px;width:27px;height:27px;border-radius:50%;border:1px solid rgba(255,255,255,.8);background:rgba(255,255,255,.15)}
.hero-next svg{position:absolute;left:8px;top:6px}
.welcome{position:absolute;left:83px;top:600px;width:602px}
.welcome h1{font-size:19px;font-weight:400;color:var(--brand);margin-bottom:8px}
.welcome p{font-size:11.3px;line-height:18.8px;margin-bottom:7px}
.services{position:absolute;left:704px;top:604px;width:195px}
.services h2{font-size:15.5px;font-weight:600;color:var(--brand);margin-bottom:12px}
.service-btn{height:35px;margin-bottom:3px;border-radius:3px;background:linear-gradient(var(--btn-top),var(--btn-bottom));color:#fff;font-size:14px;font-weight:600;display:flex;align-items:center;padding-left:27px;position:relative}
.service-btn svg{position:absolute;left:9px;top:12px}
.service-btn::after{content:"";position:absolute;left:20px;top:8px;width:1px;height:19px;background:#666}
.quick-contact{position:absolute;left:0;top:874px;width:982px;height:235px;background:var(--light)}
.quick-contact h2{position:absolute;left:0;top:18px;width:982px;text-align:center;font-size:15.5px;font-weight:400;color:var(--brand)}
.field{position:absolute;height:31px;background:#fff;border:1px solid var(--field-border);border-radius:3px;font-size:11px;color:#777;padding:9px 14px}
.field svg{position:absolute;right:8px;top:13px}
.submit{position:absolute;left:449px;top:182px;width:83px;height:31px;border-radius:3px;background:linear-gradient(#a3302f,#7a1a1c);color:#fff;font-size:13.5px;font-weight:600;text-align:center;line-height:31px}
.site-footer{position:absolute;left:0;top:1109px;width:982px;height:91px;background:var(--footer)}
.footer-links{position:absolute;left:82px;top:25px;font-size:11.3px;color:#ccc}
.footer-links span.sep{color:#666;margin:0 9px}
.copyright{position:absolute;left:82px;top:55px;font-size:11.3px;color:#bbb}
.social{position:absolute;top:41px;width:20px;height:20px;border-radius:3px}
.social.one{left:856px;background:#3b5a9a}
.social.two{left:881px;background:#3ea6d8}
</style>
</head>
<body>
<header class="site-header">
  <div class="brand"><span class="brand-mark"></span><span class="brand-name">Brightfern Supports</span></div>
  <div class="call">
    <div class="call-label">Call us</div>
    <div class="call-number">555-014-2290</div>
    <svg width="26" height="20" viewBox="0 0 26 20"><path d="M3 3c2-2 4-1 5 1l1 3c0 1-1 2-2 2 1 3 3 5 6 6 0-1 1-2 2-2l3 1c2 1 3 3 1 5-3 2-8 0-12-4S1 6 3 3z" fill="#8a8a8a"/><path d="M16 2a7 7 0 0 1 7 7M16 5a4 4 0 0 1 4 4" stroke="#aaa" stroke-width="1.5" fill="none"/></svg>
  </div>
  <div class="search"><span>Search</span><i></i><svg width="16" height="16" viewBox="0 0 16 16"><circle cx="6.5" cy="6.5" r="4.8" stroke="#777" stroke-width="2" fill="none"/><path d="M10 10l4.5 4.5" stroke="#777" stroke-width="2.4" stroke-linecap="round"/></svg></div>
</header>

<nav class="main-nav">
  <ul>
    <li class="active" style="width:78px">Home</li>
    <li style="width:108px">About us</li>
    <li style="width:96px">Services</li>
    <li style="width:106px">Our Team</li>
    <li style="width:85px">Events</li>
    <li style="width:121px">Contact us</li>
    <li style="width:113px">Locations</li>
    <li style="width:111px">Resources</li>
  </ul>
</nav>

<section class="hero" role="img" aria-label="Photo of a climber in a red jacket raising an ice axe on a snowy mountain summit">
  <div class="hero-caption">
    <p>Building abilities</p>
    <p>Creating opportunities</p>
    <p>Developing relationships</p>
  </div>
  <div class="hero-next"><svg width="9" height="14" viewBox="0 0 9 14"><path d="M2 2l5 5-5 5" stroke="#fff" stroke-width="1.5" fill="none"/></svg></div>
</section>

<main>
  <article class="welcome">
    <h1>Welcome to Brightfern Supports</h1>
    <p>Etiam commodo, ante id interdum viverra, mi enim adipiscing ipsum, sed consequat ante orci vitae mauris. Donec semper in tortor dignissim laoreet. Sed commodo ac tortor a viverra. Donec rutrum urna eu enim iaculis dictum. Phasellus posuere urna a dui porttitor, a tempus nisl ultricies. Etiam congue lobortis interdum. Nulla a porta ligula. Phasellus placerat quis elit vel mattis. Mauris consectetur diam vel tellus ultricies convallis sit amet a nulla. Donec vel faucibus enim. Nullam tincidunt, dui ac gravida pretium, tortor lectus consectetur nibh, eu placerat nisl purus nec ipsum. Sed laoreet eros id tempus tincidunt.</p>
    <p>Sed pellentesque nulla dapibus, laoreet nibh at, commodo erat. Nullam posuere, ipsum blandit aliquam fringilla, nulla lectus venenatis enim, nec suscipit risus nisi porta felis. Aenean semper est erat, ac ultrices metus malesuada ut. In ipsum nisi, eleifend pellentesque commodo ac, sollicitudin a metus. Aliquam quis dui consequat enim sceleris-que vehicula. Donec ullamcorper pharetra auctor. Praesent fringilla ligula sed quam dapibus sollicitudin.</p>
  </article>

  <aside class="services">
    <h2>Our Services</h2>
    <div class="service-btn"><svg width="6" height="9" viewBox="0 0 6 9"><path d="M1 1l3.5 3.5L1 8" stroke="#ccc" stroke-width="1.3" fill="none"/></svg>Employment</div>
    <div class="service-btn"><svg width="6" height="9" viewBox="0 0 6 9"><path d="M1 1l3.5 3.5L1 8" stroke="#ccc" stroke-width="1.3" fill="none"/></svg>Client Supports</div>
    <div class="service-btn"><svg width="6" height="9" viewBox="0 0 6 9"><path d="M1 1l3.5 3.5L1 8" stroke="#ccc" stroke-width="1.3" fill="none"/></svg>SLS Services</div>
    <div class="service-btn"><svg width="6" height="9" viewBox="0 0 6 9"><path d="M1 1l3.5 3.5L1 8" stroke="#ccc" stroke-width="1.3" fill="none"/></svg>Residential Services</div>
    <div class="service-btn"><svg width="6" height="9" viewBox="0 0 6 9"><path d="M1 1l3.5 3.5L1 8" stroke="#ccc" stroke-width="1.3" fill="none"/></svg>Work Crew/Day Program</div>
  </aside>
</main>

<section class="quick-contact">
  <h2>Quick Contact</h2>
  <div class="field" style="left:91px;top:60px;width:185px">Name</div>
  <div class="field" style="left:295px;top:60px;width:185px">E-mail</div>
  <div class="field" style="left:500px;top:60px;width:186px">Phone</div>
  <div class="field" style="left:704px;top:60px;width:186px">Service Type<svg width="10" height="6" viewBox="0 0 10 6"><path d="M0 0h10L5 6z" fill="#999"/></svg></div>
  <div class="field" style="left:91px;top:102px;width:800px;height:65px">Message</div>
  <div class="submit">SUBMIT</div>
</section>

<footer class="site-footer">
  <div class="footer-links">Home<span class="sep">|</span>About us<span class="sep">|</span>Services<span class="sep">|</span>Our Team<span class="sep">|</span>Events<span class="sep">|</span>Contact us<span class="sep">|</span>Locations<span class="sep">|</span>Resources</div>
  <div class="copyright">Copyright © 2014&nbsp; Brightfern Supports.&nbsp;&nbsp; All rights reserved.</div>
  <span class="social one"></span>
  <span class="social two"></span>
</footer>
</body>
</html>
```